Interior Design/Decor and Staging Website

Current website: www.bluefinchinteriors.example but need something lighter and more appealing. Logo is also being changed. I would like a clean cut look, modern and professional. Would like a slideshow for portfolio pictures, social media icons and logos of where the work has been featured: ORVA, Nest Wares, Durmalen, Theodore Vance, Plaza Furnishings, etc.

Target Market(s)

interior design and interior decor clients, both local and international.

Industry/Entity Type

Home Improvement

Number of Pages Required

5+ page

Font styles to use
Sans Serif

Requirements
Nice to have
• Testimonial page and Roomly reviews.

```html
<!DOCTYPE html>
<html lang="en">
<head>
<meta charset="utf-8">
<title>Bluefinch Interiors</title>
<link rel="stylesheet" href="https://fonts.googleapis.com/css2?family=Cinzel:wght@400;600&family=Open+Sans:ital,wght@0,400;0,600;1,400&display=swap">
<style>
:root{
  --gold:#c9a55a;
  --gold-light:#dcc187;
  --gold-dark:#b08d47;
  --header-dark:#6c6c6c;
  --text:#555;
  --footer:#565656;
  --footer-bar:#4b4b4b;
  --footer-text:#eeeeee;
  --band:#f1f1f1;
  --white:#fff;
  --link:#2f86b8;
  --star:#e8902a;
}
*{margin:0;padding:0;box-sizing:border-box}
html,body{width:1200px;height:2535px;overflow:hidden;background:var(--white)}
body{font-family:"Open Sans",Arial,sans-serif;color:var(--text);position:relative}
.page{position:relative;width:1200px;height:2535px}
.abs{position:absolute}

/* header */
.site-header{left:0;top:0;width:1200px;height:155px;background:linear-gradient(#838383,var(--header-dark));border-top:4px solid var(--gold-light)}
.brand{left:100px;top:38px;display:flex;align-items:center;gap:12px;color:var(--gold-light);font-family:"Cinzel",Georgia,serif;font-size:26px;line-height:30px;font-weight:600}
.brand-dot{width:40px;height:40px;border-radius:50%;background:var(--gold-light)}
.social{right:98px;top:38px;display:flex;gap:10px}
.social span{width:38px;height:38px;border-radius:50%;background:#9a9a9a;border:3px solid #d7d7d7;display:block}
.social span:last-child{background:var(--gold-light)}
.nav{right:82px;top:95px;display:flex;gap:44px;font-family:"Cinzel",Georgia,serif;font-size:14px;color:#f2f2f2;letter-spacing:.5px}
.nav .active{color:var(--gold-light)}

/* hero */
.hero{left:0;top:155px;width:1200px;height:513px;background:linear-gradient(100deg,#e9e6e1 0%,#d6cfc6 30%,#a78a6a 55%,#8a6547 70%,#d9d6d1 85%,#c9c9c9 100%)}
.hero-caption{left:640px;top:535px;color:var(--white);font-family:"Cinzel",Georgia,serif;font-size:25px;line-height:28px}
.hero-arrow{top:385px}

/* welcome */
.section-title{font-family:"Cinzel",Georgia,serif;color:var(--gold);font-weight:400;text-align:center;letter-spacing:1px}
.welcome-title{left:0;top:728px;width:1200px;font-size:31px}
.welcome-text{left:165px;top:776px;width:870px;text-align:center;font-size:12.5px;line-height:20px;color:#444}
.btn{display:inline-flex;align-items:center;justify-content:center;font-size:14px;height:46px}
.btn-gold{background:linear-gradient(#d9bd7c,var(--gold-dark));color:var(--white)}
.btn-outline{border:1px solid #e1d2ad;color:var(--gold);background:var(--white)}
.welcome-actions{left:414px;top:852px;display:flex;gap:14px}
.welcome-actions .btn{width:156px}

/* services */
.services{left:0;top:957px;width:1200px;height:606px;background:linear-gradient(160deg,#f4f3ef 0%,#e6e5df 40%,#eeece6 70%,#e3e2dc 100%);border-top:1px solid #e7e7e7}
.services-title{left:0;top:1012px;width:1200px;font-size:31px}
.service-card{top:1200px;width:306px;height:286px;background:var(--white);box-shadow:0 6px 12px rgba(0,0,0,.18);text-align:center;padding-top:96px}
.service-photo{top:1097px;width:192px;height:192px;border-radius:50%;border:6px solid #e4e4e4;box-shadow:0 2px 6px rgba(0,0,0,.15)}
.service-card h3{font-family:"Cinzel",Georgia,serif;font-weight:400;font-size:18px;color:#333;letter-spacing:1px}
.service-card p{font-size:12.5px;line-height:19px;color:#444;margin:10px 30px 0}
.service-card .btn{height:37px;width:104px;font-size:12px;margin-top:14px}

/* testimonials */
.block-title{font-family:"Cinzel",Georgia,serif;color:var(--gold);font-size:30px;font-weight:400;letter-spacing:1px}
.testi-title{left:95px;top:1610px}
.reviews-title{left:686px;top:1610px}
.quote{left:122px;top:1686px;width:530px;font-size:12px;line-height:23px;font-style:italic;color:#555}
.quote-mark{font-family:Georgia,serif;font-size:48px;color:#ccc;line-height:1}
.quote-close{font-family:Georgia,serif;font-style:normal;font-size:36px;color:#ccc;line-height:0;vertical-align:-14px;margin-left:6px}
.avatar{left:102px;top:1780px;width:114px;height:114px;border-radius:50%;background:radial-gradient(#c9a48a,#8d6d58);border:5px solid #e8d6ad}
.person{left:238px;top:1820px}
.person b{display:block;color:var(--gold);font-size:12px;font-weight:600;letter-spacing:.5px}
.person span{font-size:12px;color:#333}
.pager{display:flex;gap:2px}
.pager i{width:12px;height:12px;border-radius:50%;background:#bbb;display:block}
.review-box{left:692px;top:1658px;width:410px;height:216px;background:#f3f3f3;border:1px solid #e0e0e0;padding:22px 22px}
.review-box p{font-size:12.5px;line-height:22px;color:#555}
.rating{display:flex;align-items:center;gap:10px;margin-top:10px;font-size:12px;color:var(--link)}

/* clients */
.clients{left:0;top:1945px;width:1200px;height:263px;background:var(--band)}
.clients-title{left:0;top:1990px;width:1200px;font-size:30px}
.client-logo{top:2058px;width:168px;height:92px;background:var(--white);border:1px solid #e3e3e3;box-shadow:0 1px 3px rgba(0,0,0,.08);display:flex;align-items:center;justify-content:center;font-weight:600;font-size:17px;color:#3a3a3a;text-align:center;line-height:20px}

/* footer */
.site-footer{left:0;top:2208px;width:1200px;height:267px;background:var(--footer)}
.footer-brand{left:100px;top:2285px;font-size:21px;line-height:25px}
.footer-brand .brand-dot{width:32px;height:32px}
.footer-col{color:var(--footer-text)}
.footer-head{font-family:"Cinzel",Georgia,serif;font-size:15px;color:#f3f3f3;letter-spacing:.5px}
.quicklinks{left:328px;top:2245px}
.quicklinks ul{list-style:none;margin-top:14px}
.quicklinks li{font-size:12.5px;line-height:28px;color:var(--footer-text)}
.chat{left:543px;top:2245px}
.chat-row{display:flex;gap:12px;font-size:12.5px;line-height:25px;margin-top:10px;width:250px;color:var(--footer-text)}
.chat-row svg{flex:none;margin-top:6px}
.contact{left:850px;top:2245px}
.field{width:252px;height:32px;border:1px solid #9a9a9a;background:#5e5e5e;color:#ddd;font-size:12px;padding:7px 10px;margin-top:8px}
.field.area{height:60px}
.submit{width:86px;height:30px;background:var(--gold);color:var(--white);font-size:12px;display:flex;align-items:center;justify-content:center;margin-top:12px}
.footer-bar{left:0;top:2475px;width:1200px;height:60px;background:var(--footer-bar);color:#ddd;font-size:12px;display:flex;align-items:center;justify-content:space-between;padding:0 100px}
.bar-social{display:flex;align-items:center;gap:16px}
.bar-social i{width:9px;height:9px;border-radius:50%;background:#ddd;display:block}
</style>
</head>
<body>
<div class="page">

  <header class="site-header abs">
    <div class="brand abs"><span class="brand-dot"></span><span>Bluefinch<br>Interiors</span></div>
    <div class="social abs" aria-label="Social media links">
      <span></span><span></span><span></span><span></span><span></span>
    </div>
    <nav class="nav abs"><span class="active">Home</span><span>Services</span><span>Gallery</span><span>Contact</span></nav>
  </header>

  <section class="hero abs" role="img" aria-label="Portfolio slideshow photo of a bright open-plan living room and kitchen with wood floors"></section>
  <svg class="hero-arrow abs" style="left:30px" width="18" height="46" viewBox="0 0 18 46"><polyline points="16,2 2,23 16,44" fill="none" stroke="rgba(255,255,255,.7)" stroke-width="2"/></svg>
  <svg class="hero-arrow abs" style="left:1152px" width="18" height="46" viewBox="0 0 18 46"><polyline points="2,2 16,23 2,44" fill="none" stroke="rgba(255,255,255,.7)" stroke-width="2"/></svg>
  <div class="hero-caption abs">South Florida<br>Interior Decor</div>

  <h1 class="section-title welcome-title abs">Welcome to Bluefinch Interiors</h1>
  <p class="welcome-text abs">From condos to estates, we can help you achieve the style you want.Have your house professionally decorated for a quicker sale.Decor outdated? Need new flooring or kitchen cabinets? We can help you.From condos to estates, we can help you achieve the style you want.Have your house professionally decorated for a quicker sale.Decor outdated? Need new flooring or kitchen cabinets? We can help you.</p>
  <div class="welcome-actions abs"><span class="btn btn-gold">View more info</span><span class="btn btn-outline">Meet our clients</span></div>

  <section class="services abs" role="img" aria-label="Faded background photo of a porch overlooking greenery"></section>
  <h2 class="section-title services-title abs">Design Services</h2>

  <article class="service-card abs" style="left:102px"><h3>Interior Decor</h3><p>From condos to estates, we can help you achieve the style you want.From condos to estates, we can help you achieve the style you want.</p><span class="btn btn-gold">Read More</span></article>
  <article class="service-card abs" style="left:448px"><h3>Home Staging</h3><p>From condos to estates, we can help you achieve the style you want.From condos to estates, we can help you achieve the style you want.</p><span class="btn btn-gold">Read More</span></article>
  <article class="service-card abs" style="left:793px"><h3>Restyle &amp; Redesign</h3><p>From condos to estates, we can help you achieve the style you want.From condos to estates, we can help you achieve the style you want.</p><span class="btn btn-gold">Read More</span></article>
  <div class="service-photo abs" style="left:159px;background:radial-gradient(#f3f1ea,#b9c2a8)" role="img" aria-label="Photo of a bright room with a staircase and plants"></div>
  <div class="service-photo abs" style="left:505px;background:radial-gradient(#e8e2d6,#9b7a55)" role="img" aria-label="Photo of a leather lounge chair with cushions"></div>
  <div class="service-photo abs" style="left:850px;background:radial-gradient(#e7d8cc,#b07a62)" role="img" aria-label="Photo of designers reviewing plans with clients"></div>

  <h2 class="block-title testi-title abs">Our Testimonials</h2>
  <span class="quote-mark abs" style="left:96px;top:1672px">&ldquo;</span>
  <p class="quote abs">From condos to estates, we can help you achieve the style you want.Have your house professionally decorated for a quicker sale.Decor outdated? Need new flooring or kitchen cabinets? We can help you.From condos to estates, we can help you achieve the style you want...<span class="quote-close">&rdquo;</span></p>
  <div class="avatar abs" role="img" aria-label="Portrait photo of the reviewer"></div>
  <div class="person abs"><b>MARLON TESSEL</b><span>Business man</span></div>
  <div class="pager abs" style="left:520px;top:1835px"><i></i><i></i></div>

  <h2 class="block-title reviews-title abs">Our Roomly Reviews</h2>
  <div class="review-box abs">
    <p>From condos to estates, we can help you achieve the style you want.Have your house professionally decorated for a quicker sale.Decor outdated? Need new flooring or kitchen cabinets? We can help you.From condos to estates, we can help you achieve the style you want...</p>
    <div class="rating">
      <svg width="74" height="13" viewBox="0 0 74 13">
        <g fill="var(--star)">
          <polygon points="6.5,0 8.2,4.5 13,4.8 9.3,7.8 10.5,12.5 6.5,9.8 2.5,12.5 3.7,7.8 0,4.8 4.8,4.5"/>
          <polygon transform="translate(15)" points="6.5,0 8.2,4.5 13,4.8 9.3,7.8 10.5,12.5 6.5,9.8 2.5,12.5 3.7,7.8 0,4.8 4.8,4.5"/>
          <polygon transform="translate(30)" points="6.5,0 8.2,4.5 13,4.8 9.3,7.8 10.5,12.5 6.5,9.8 2.5,12.5 3.7,7.8 0,4.8 4.8,4.5"/>
          <polygon transform="translate(45)" points="6.5,0 8.2,4.5 13,4.8 9.3,7.8 10.5,12.5 6.5,9.8 2.5,12.5 3.7,7.8 0,4.8 4.8,4.5"/>
          <polygon transform="translate(60)" points="6.5,0 6.5,9.8 2.5,12.5 3.7,7.8 0,4.8 4.8,4.5"/>
        </g>
      </svg>
      <span>645 Reviews</span>
    </div>
  </div>
  <div class="pager abs" style="left:1063px;top:1822px"><i></i><i></i></div>

  <section class="clients abs"></section>
  <h2 class="section-title clients-title abs">Companies Logos Features as Clients</h2>
  <svg class="abs" style="left:46px;top:2092px" width="10" height="24" viewBox="0 0 10 24"><polyline points="9,1 1,12 9,23" fill="none" stroke="#ccc" stroke-width="1.5"/></svg>
  <div class="client-logo abs" style="left:103px">ORVA</div>
  <div class="client-logo abs" style="left:308px">Nest Wares</div>
  <div class="client-logo abs" style="left:513px">Durmalen</div>
  <div class="client-logo abs" style="left:718px">Theodore<br>Vance</div>
  <div class="client-logo abs" style="left:925px">Plaza<br>Furnishings</div>
  <svg class="abs" style="left:1142px;top:2092px" width="10" height="24" viewBox="0 0 10 24"><polyline points="1,1 9,12 1,23" fill="none" stroke="#ccc" stroke-width="1.5"/></svg>

  <footer class="site-footer abs"></footer>
  <div class="brand footer-brand abs"><span class="brand-dot"></span><span>Bluefinch<br>Interiors</span></div>
  <div class="footer-col quicklinks abs">
    <div class="footer-head">Quicklinks</div>
    <ul><li>&rsaquo; Home</li><li>&rsaquo; Services</li><li>&rsaquo; Gallery</li><li>&rsaquo; Contact</li></ul>
  </div>
  <div class="footer-col chat abs">
    <div class="footer-head">Let's Chat!</div>
    <div class="chat-row"><svg width="10" height="13" viewBox="0 0 10 13"><path d="M5 0a5 5 0 0 1 5 5c0 3.5-5 8-5 8S0 8.5 0 5a5 5 0 0 1 5-5z" fill="#eee"/><circle cx="5" cy="5" r="1.8" fill="#565656"/></svg><span>Harlow Lane, Fennick, 6020 Western Australia</span></div>
    <div class="chat-row"><svg width="13" height="10" viewBox="0 0 13 10"><rect width="13" height="10" fill="#eee"/><polyline points="0,0 6.5,5.5 13,0" fill="none" stroke="#565656" stroke-width="1.2"/></svg><span>Email:hello@bluefinchinteriors.example</span></div>
    <div class="chat-row"><svg width="12" height="12" viewBox="0 0 12 12"><rect width="12" height="12" rx="2" fill="#eee"/><path d="M3.5 2.5l1.5 1.5-.8 1.2c.6 1.2 1.4 2 2.6 2.6l1.2-.8 1.5 1.5-1 1c-3 0-6-3-6-6z" fill="#565656"/></svg><span>Phone: +1300 555 014</span></div>
  </div>
  <div class="footer-col contact abs">
    <div class="footer-head">Contact Details</div>
    <div class="field" style="margin-top:14px">Enter your name</div>
    <div class="field">Email address</div>
    <div class="field area">Enter your massage</div>
    <div class="submit">Submit</div>
  </div>
  <div class="footer-bar abs">
    <span>&copy; bluefinchinteriors.example 2016. All rights reserved</span>
    <span class="bar-social">Connct with our social network : <i></i><i></i><i></i><i></i><i></i></span>
  </div>

</div>
</body>
</html>
```